RT Blacktop Works needs awesome postcard design

Business to business post card design needed. We are an asphalt paving contractor looking to attract commercial and industrial customers who need pavement replacement and repairs. We do: Asphalt paving, milling, crack filling and striping.

Postcard should have the following words:
RT Blacktop Works
www.rtblacktopworks.example
Asphalt Paving
Milling
Hot Rubber Crack Filling
Striping

Michigan's Premier Paving Contractor
(555) 827-1963

Address for return area on card:
RT Blacktop Works
48213 Fenwick
New Boston, MI 00000

Target Market(s)

Building owners and property managers

Industry/Entity Type

Ashpalt Paving

Font styles to use
Sans Serif

Requirements
Must have
• Logo, phone number (555) 827-1963, tagline: "Michigan's Premier Paving Contractor" website address and: Paving, milling, hot rubber crack filling, seal coating
Nice to have
• Picture of a newly paved parking lot with or without stripes
Should not have
• Homeowner driveway - WE DO NOT WANT TO ATTRACT RESIDENTIAL WORK

```html
<!DOCTYPE html>
<html lang="en">
<head>
<meta charset="utf-8">
<title>RT Blacktop Works – Postcard</title>
<link rel="stylesheet" href="https://fonts.googleapis.com/css2?family=Montserrat:wght@400;700;800&display=swap">
<style>
  :root {
    --sky: #d3dbe2;
    --storefront: #d8c6a2;
    --trees: #5d7642;
    --concrete: #a3a3a0;
    --asphalt-light: #5c5d60;
    --asphalt-mid: #3a3a3c;
    --asphalt-dark: #1f1f20;
    --white: #ffffff;
    --ink: #1d1d1d;
    --blue: #25439a;
    --orange: #f28a21;
    --frame: #ffffff;
  }
  * { margin: 0; padding: 0; box-sizing: border-box; }
  html, body {
    width: 1200px; height: 954px; overflow: hidden;
    background: #ffffff;
    font-family: "Montserrat", Arial, sans-serif;
  }
  .postcard {
    position: relative; width: 1200px; height: 954px; overflow: hidden;
    background: var(--asphalt-dark);
  }
  .hero-photo {
    position: absolute; inset: 0 0 200px 0;
    background:
      radial-gradient(ellipse 420px 90px at 180px 270px, rgba(170,170,166,.55), rgba(170,170,166,0) 100%),
      radial-gradient(ellipse 520px 120px at 420px 200px, rgba(120,118,108,.45), rgba(120,118,108,0) 100%),
      radial-gradient(ellipse 260px 60px at 700px 95px, rgba(80,110,60,.6), rgba(80,110,60,0) 100%),
      linear-gradient(180deg,
        var(--sky) 0%,
        var(--storefront) 3%,
        #cdb999 8%,
        var(--trees) 11%,
        #6f7f5a 13.5%,
        var(--concrete) 15%,
        #7a7a7b 19%,
        var(--asphalt-light) 27%,
        #474749 40%,
        var(--asphalt-mid) 55%,
        #2a2a2b 78%,
        var(--asphalt-dark) 100%);
  }
  .headline {
    position: absolute; left: 0; right: 0; top: 292px;
    text-align: center; color: var(--white);
  }
  .headline .tagline-top {
    display: block; font-weight: 400; font-size: 55px; letter-spacing: 2px; line-height: 1;
  }
  .headline .tagline-main {
    display: block; font-weight: 800; font-size: 75px; letter-spacing: 1px; line-height: 1; margin-top: 12px;
  }
  .services {
    position: absolute; top: 461px; left: 0; width: 1200px; height: 260px;
  }
  .service {
    position: absolute; top: 0; width: 245px; text-align: center;
  }
  .service-photo {
    width: 245px; height: 190px; border: 8px solid var(--frame);
  }
  .service-name {
    margin-top: 12px; color: var(--white);
    font-weight: 700; font-size: 25px; line-height: 1.2; letter-spacing: .3px;
    height: 60px; display: flex; align-items: center; justify-content: center;
  }
  .s1 { left: 58px; } .s2 { left: 341px; } .s3 { left: 626px; } .s4 { left: 910px; }
  .s1 .service-photo {
    background:
      radial-gradient(ellipse 90px 50px at 60px 85px, rgba(214,168,40,.85), rgba(214,168,40,0) 100%),
      radial-gradient(ellipse 110px 45px at 150px 110px, rgba(190,150,45,.8), rgba(190,150,45,0) 100%),
      linear-gradient(180deg, #9aa3ad 0%, #b3b7b8 22%, #8b7a4a 45%, #6d6040 65%, #4b4a47 80%, #3e3e3e 100%);
  }
  .s2 .service-photo {
    background:
      radial-gradient(ellipse 80px 45px at 150px 85px, rgba(235,235,232,.9), rgba(235,235,232,0) 100%),
      radial-gradient(ellipse 45px 30px at 55px 90px, rgba(90,90,92,.7), rgba(90,90,92,0) 100%),
      linear-gradient(180deg, #5f86c4 0%, #9db4d6 28%, #cfd6de 42%, #8f9294 55%, #a7a198 72%, #8c877f 100%);
  }
  .s3 .service-photo {
    background:
      radial-gradient(ellipse 40px 60px at 50px 20px, rgba(60,80,110,.8), rgba(60,80,110,0) 100%),
      radial-gradient(ellipse 30px 80px at 120px 70px, rgba(225,200,40,.7), rgba(225,200,40,0) 100%),
      radial-gradient(ellipse 90px 30px at 170px 150px, rgba(40,40,40,.75), rgba(40,40,40,0) 100%),
      linear-gradient(160deg, #c3c3c1 0%, #b0b0ae 50%, #8f8f8d 80%, #6a6a69 100%);
  }
  .s4 .service-photo {
    background:
      radial-gradient(ellipse 45px 90px at 70px 70px, rgba(226,120,40,.9), rgba(226,120,40,0) 100%),
      radial-gradient(ellipse 40px 70px at 170px 80px, rgba(240,240,240,.85), rgba(240,240,240,0) 100%),
      linear-gradient(180deg, #b0694d 0%, #9b5a45 30%, #4a4a4c 55%, #2f2f31 100%);
  }
  .footer { position: absolute; left: 0; top: 0; width: 1200px; height: 954px; pointer-events: none; }
  .brand {
    position: absolute; left: 60px; top: 822px;
    display: flex; align-items: center; gap: 14px;
  }
  .brand-mark { width: 34px; height: 34px; background: var(--ink); }
  .brand-name { color: var(--ink); font-weight: 800; font-size: 40px; letter-spacing: -.5px; line-height: 1; }
  .estimate {
    position: absolute; left: 560px; width: 640px; top: 765px; height: 56px;
    display: flex; align-items: center; justify-content: center;
    color: var(--white); font-weight: 800; font-size: 32px; letter-spacing: .5px;
  }
  .contact {
    position: absolute; left: 630px; top: 838px; display: flex; align-items: center; gap: 16px;
    color: var(--white);
  }
  .phone-icon { width: 60px; height: 80px; }
  .contact-lines { display: flex; flex-direction: column; }
  .phone { font-weight: 800; font-size: 59px; line-height: 1; letter-spacing: .5px; }
  .website { font-weight: 700; font-size: 26px; line-height: 1; margin-top: 10px; }
</style>
</head>
<body>
<main class="postcard">
  <div class="hero-photo" role="img" aria-label="Newly paved commercial parking lot with fresh yellow stripes in front of a shopping plaza"></div>

  <h1 class="headline">
    <span class="tagline-top">MICHIGAN’S PREMIER</span>
    <span class="tagline-main">PAVING CONTRACTOR</span>
  </h1>

  <section class="services">
    <div class="service s1">
      <div class="service-photo" role="img" aria-label="Asphalt paving machine laying a new surface"></div>
      <p class="service-name">ASPHALT<br>PAVING</p>
    </div>
    <div class="service s2">
      <div class="service-photo" role="img" aria-label="Milling machine removing old pavement into a truck"></div>
      <p class="service-name">MILLING</p>
    </div>
    <div class="service s3">
      <div class="service-photo" role="img" aria-label="Worker applying hot rubber crack filler to pavement"></div>
      <p class="service-name">HOT RUBBER<br>CRACK FILLING</p>
    </div>
    <div class="service s4">
      <div class="service-photo" role="img" aria-label="Crew member painting white crosswalk stripes"></div>
      <p class="service-name">STRIPING</p>
    </div>
  </section>

  <svg class="footer" viewBox="0 0 1200 954" aria-hidden="true">
    <polygon points="0,748 490,748 597,954 0,954" fill="var(--white)"/>
    <polygon points="497,765 1200,765 1200,821 526,821" fill="var(--blue)"/>
    <polygon points="526,821 1200,821 1200,954 597,954" fill="var(--orange)"/>
  </svg>

  <div class="brand">
    <span class="brand-mark"></span>
    <span class="brand-name">RT Blacktop Works</span>
  </div>

  <p class="estimate">GET FREE ESTIMATE TODAY!</p>

  <div class="contact">
    <svg class="phone-icon" viewBox="0 0 60 80" aria-hidden="true">
      <rect x="12" y="3" width="38" height="68" rx="7" fill="none" stroke="var(--white)" stroke-width="5"/>
      <rect x="18" y="12" width="26" height="44" fill="var(--white)" opacity=".35"/>
      <circle cx="31" cy="63" r="3" fill="var(--white)"/>
      <path d="M4 46 q-3 20 17 29 l14 3 q6 0 6 -6 l-4 -13 q-4 -6 -12 -4 z" fill="var(--white)"/>
    </svg>
    <div class="contact-lines">
      <span class="phone">(555) 827-1963</span>
      <span class="website">www.rtblacktopworks.example</span>
    </div>
  </div>
</main>
</body>
</html>
```